Postcard Mailer

We are a pizza pub that is the only local restaurant that offers and delivers pizza, burgers, salads and wings.

We just opened and want to send out a postcard to the community. thinking on one side a nice design with pics etc. then on the back a list of our daily food and drink specials.

Restaurant

eb1f27

```html
<!DOCTYPE html>
<html lang="en">
<head>
<meta charset="utf-8">
<title>Rosa and Marco – Postcard Mailer</title>
<link href="https://fonts.googleapis.com/css2?family=Archivo+Black&family=Open+Sans:wght@400;600;700;800&family=Roboto+Slab:wght@700&display=swap" rel="stylesheet">
<style>
  :root {
    --brand-red: #eb1f27;
    --leaf-green: #3f8f1f;
    --char: #231f1f;
    --char-warm: #3a2a24;
    --crust-yellow: #f5e04a;
    --paper: #ffffff;
    --backdrop: #e6e6e6;
    --rule: #c9c9c9;
    --ink: #ffffff;
  }
  * { box-sizing: border-box; margin: 0; padding: 0; }
  html, body { width: 858px; height: 1200px; overflow: hidden; background: var(--backdrop); }
  body { position: relative; font-family: "Open Sans", sans-serif; }

  .card { position: absolute; left: 101px; width: 653px; height: 503px; overflow: hidden; }
  .card--front { top: 74px; background: linear-gradient(160deg, var(--char-warm) 0%, var(--char) 60%); }
  .card--back { top: 620px; background: var(--paper); }

  /* Front */
  .hero-photo { position: absolute; left: 0; top: 0; width: 560px; height: 380px; }
  .headline-banner { position: absolute; left: 0; top: 2px; width: 530px; height: 65px; background: var(--brand-red);
    clip-path: polygon(0 0, 100% 0, 96% 100%, 0 100%); }
  .headline { position: absolute; left: 20px; top: 0; font-family: "Archivo Black", sans-serif; font-size: 56px; line-height: 65px; color: var(--ink); letter-spacing: 1px; }
  .menu-banner { position: absolute; left: 0; top: 72px; width: 414px; height: 41px; background: var(--leaf-green);
    clip-path: polygon(0 0, 100% 0, 97% 100%, 0 100%); }
  .menu-line { position: absolute; left: 18px; top: 0; font-weight: 800; font-size: 28px; line-height: 41px; color: var(--ink); letter-spacing: .5px; }

  .side-photo { position: absolute; width: 112px; height: 102px; border: 5px solid var(--paper); }
  .side-photo--burger { left: 540px; top: -6px; transform: rotate(2deg); background: linear-gradient(160deg, #d9a25a, #8a4a22 60%, #3b241a); }
  .side-photo--salad { left: 543px; top: 100px; transform: rotate(-2deg); background: linear-gradient(150deg, #5c8f2e, #4a2e22 55%, #7fae3a); }
  .side-photo--wings { left: 540px; top: 212px; transform: rotate(3deg); background: linear-gradient(160deg, #c2571d, #7a2c12 60%, #a94a1a); }
  .side-photo--beer { left: 543px; top: 372px; transform: rotate(-4deg); width: 118px; height: 118px; background: linear-gradient(170deg, #f0c14b, #c4781b 60%, #5a3512); }

  .brand-mark { position: absolute; left: 25px; top: 318px; width: 168px; height: 150px; display: flex; flex-direction: column; align-items: center; justify-content: center; gap: 10px; }
  .brand-dot { width: 70px; height: 70px; border-radius: 50%; background: var(--ink); }
  .brand-name { font-weight: 800; font-size: 17px; color: var(--ink); letter-spacing: 1px; text-align: center; }

  .delivery { position: absolute; left: 217px; top: 375px; color: var(--ink); }
  .delivery-label { font-weight: 700; font-size: 23px; line-height: 30px; }
  .delivery-phone { font-weight: 700; font-size: 40px; line-height: 46px; color: var(--brand-red); }
  .delivery-web { font-weight: 700; font-size: 19px; line-height: 24px; }
  .delivery-address { font-weight: 700; font-size: 12px; line-height: 20px; color: var(--brand-red); text-transform: uppercase; }

  /* Back */
  .offers-panel { position: absolute; left: 0; top: 0; width: 319px; height: 421px; background: var(--char); }
  .offers-tab { position: absolute; left: 0; top: 2px; width: 134px; height: 27px; background: var(--brand-red);
    font-family: "Archivo Black", sans-serif; font-size: 23px; line-height: 27px; color: var(--ink); padding-left: 12px;
    clip-path: polygon(0 0, 100% 0, 95% 100%, 0 100%); }
  .offers-tagline { position: absolute; left: 140px; top: 3px; font-family: "Roboto Slab", serif; font-size: 10px; line-height: 12px; color: var(--ink); text-align: center; }
  .offers-col { position: absolute; top: 36px; color: var(--ink); font-size: 11px; line-height: 14px; }
  .offers-col--left { left: 15px; }
  .offers-col--right { left: 171px; }
  .offers-divider { position: absolute; left: 164px; top: 38px; height: 232px; border-left: 2px dotted var(--ink); }
  .offer { margin-bottom: 14px; }
  .offer-day { font-weight: 700; color: var(--brand-red); font-size: 11.5px; }
  .back-brand { position: absolute; left: 32px; top: 276px; }
  .back-brand .brand-dot { display: block; width: 54px; height: 54px; }
  .back-phone { position: absolute; left: 104px; top: 286px; font-weight: 700; font-size: 27px; line-height: 30px; color: var(--brand-red); white-space: nowrap; }
  .back-web { position: absolute; left: 138px; top: 318px; font-weight: 700; font-size: 11px; line-height: 14px; color: var(--ink); white-space: nowrap; }
  .photo-strip { position: absolute; left: 0; top: 346px; width: 319px; height: 76px; }
  .strip-tile { position: absolute; top: 2px; width: 76px; height: 70px; border: 4px solid var(--paper); }
  .strip-tile--burger { left: 0; transform: rotate(-3deg); background: linear-gradient(160deg, #d9a25a, #8a4a22 60%, #3b241a); }
  .strip-tile--salad { left: 76px; transform: rotate(2deg); background: linear-gradient(150deg, #5c8f2e, #4a2e22 55%, #7fae3a); }
  .strip-tile--wings { left: 154px; background: linear-gradient(160deg, #c2571d, #7a2c12 60%, #a94a1a); }
  .strip-tile--beer { left: 232px; transform: rotate(3deg); width: 84px; background: linear-gradient(170deg, #f0c14b, #c4781b 60%, #5a3512); }

  .stamp-box { position: absolute; left: 510px; top: 24px; width: 119px; height: 115px; border: 1px solid var(--rule); }
  .address-line { position: absolute; left: 353px; width: 259px; border-top: 1px solid var(--rule); }
</style>
</head>
<body>

<section class="card card--front" aria-label="Postcard front">
  <svg class="hero-photo" viewBox="0 0 560 380" role="img" aria-label="Photo of a loaded supreme pizza with pepperoni, tomatoes, peppers and mushrooms">
    <defs>
      <radialGradient id="pizzaTone" cx="50%" cy="35%" r="70%">
        <stop offset="0" stop-color="#e8c98a"/>
        <stop offset=".55" stop-color="#c8643a"/>
        <stop offset="1" stop-color="#7a3a22"/>
      </radialGradient>
    </defs>
    <path d="M0 0 H545 V300 Q300 340 0 255 Z" fill="url(#pizzaTone)"/>
    <path d="M0 255 Q300 340 545 300 L545 312 Q300 356 0 268 Z" fill="var(--crust-yellow)"/>
  </svg>

  <div class="headline-banner"><h1 class="headline">WE'RE OPEN!</h1></div>
  <div class="menu-banner"><p class="menu-line">PIZZA | BURGER | SALAD</p></div>

  <div class="side-photo side-photo--burger" role="img" aria-label="Photo of a cheeseburger"></div>
  <div class="side-photo side-photo--salad" role="img" aria-label="Photo of a steak salad"></div>
  <div class="side-photo side-photo--wings" role="img" aria-label="Photo of chicken wings"></div>
  <div class="side-photo side-photo--beer" role="img" aria-label="Photo of a craft beer flight"></div>

  <div class="brand-mark">
    <span class="brand-dot"></span>
    <span class="brand-name">ROSA AND MARCO</span>
  </div>

  <div class="delivery">
    <p class="delivery-label">For Home Delivery call :</p>
    <p class="delivery-phone">(555) 014-2290</p>
    <p class="delivery-web">www.rosaandmarcopizza.com</p>
    <p class="delivery-address">742 Harbor Lane Seaside, NC 28400</p>
  </div>
</section>

<section class="card card--back" aria-label="Postcard back">
  <div class="offers-panel">
    <div class="offers-tab">OFFERS</div>
    <p class="offers-tagline">**OUR ROSA BURGERS<br>ARE A MUST TRY**</p>

    <div class="offers-col offers-col--left">
      <div class="offer"><p class="offer-day">Daily Lunch Special</p><p>2 Slices + Drink $4.95</p></div>
      <div class="offer"><p class="offer-day">Monday</p><p>Buy 1 Medium Pizza<br>Get 1 Free<br>$1 Domestic Beers</p></div>
      <div class="offer"><p class="offer-day">Tuesday</p><p>Medium Pizza $7.95<br>50 cent wings<br>$1.50 Drafts</p></div>
      <div class="offer"><p class="offer-day">Wednesday</p><p>Classic Burger + Beer $5.95<br>$2.50 Cinnamon Shots</p></div>
    </div>
    <div class="offers-divider"></div>
    <div class="offers-col offers-col--right">
      <div class="offer"><p class="offer-day">Thursday</p><p>$1 Slice Night<br>$2.50 Craft Beers</p></div>
      <div class="offer"><p class="offer-day">Friday</p><p>2 Medium Pizzas $15.95<br>$2 Glasses of Wine</p></div>
      <div class="offer"><p class="offer-day">Saturday</p><p>1/2 Price Salads<br>$3 Vodka Drinks<br>$2.50 House IPA</p></div>
      <div class="offer"><p class="offer-day">Sunday</p><p>Large Pizza $9.95<br>$3 Bloody Mary's<br>&amp; Mimosa's</p></div>
    </div>

    <div class="back-brand"><span class="brand-dot"></span></div>
    <p class="back-phone">(555) 014-2290</p>
    <p class="back-web">www.rosaandmarcopizza.com</p>

    <div class="photo-strip">
      <div class="strip-tile strip-tile--burger" role="img" aria-label="Photo of a cheeseburger"></div>
      <div class="strip-tile strip-tile--salad" role="img" aria-label="Photo of a steak salad"></div>
      <div class="strip-tile strip-tile--wings" role="img" aria-label="Photo of chicken wings"></div>
      <div class="strip-tile strip-tile--beer" role="img" aria-label="Photo of a craft beer flight"></div>
    </div>
  </div>

  <div class="stamp-box"></div>
  <div class="address-line" style="top:248px"></div>
  <div class="address-line" style="top:278px"></div>
  <div class="address-line" style="top:307px"></div>
  <div class="address-line" style="top:336px"></div>
</section>

</body>
</html>
```